Verdant Grain Collective needs packaging design for 500g Hemp Seed Pouch

We need a packaging design for the release of our Australian sourced Super Healthy, Nutritious super food HEMP SEED.

The verdant Grain collective - food, fibre, fuel, building, medicine
We are a start up company who is very Passionate about Hemp, rebuilding the hemp industry through inspiration, education and distribution of all things hemp.

This Hemp Seed packaging will be our first product launch

Kernel of FIELD SEEDS 500gram

needs to communicate 3 things, that Hemp seeds:
1. TASTE GREAT
2. EASY TO USE
3. GOOD FOR YOU

other Features of hemp seeds is that they are :
Vegan
Paleo
Raw
Sustainable
High in protein
High in Omega 3 + 6 EFA
Anti allergenic

we would like to see designs that work with our current logo and colouring of orange and black. premium and stylish that says healthy

the pouches will be '500g' meaning they will hold 500grams of hulled hemp seeds.

with dimensions of
170mm x 250mm
see attached photo of competitors hemp protein pouch as example of pouch design

see attached for current logo designs and colouring
also see attached concept sketch we are not married to this sketch it is just as a guideline for elements that should be included.

final design should feel healthy clean and safe for consumption:)
with an emphasis on being PremiumAustralian seed soured from from pristine Tasmania

Target Market(s)

Health conscious

Requirements
Must have
• map of Australia or show that it is Australian in some way
Nice to have
• Spoon of hemp seeds or picture of Grain Cores

```html
<!DOCTYPE html>
<html lang="en">
<head>
<meta charset="utf-8">
<title>Kernel of Field Seeds – 500g Pouch</title>
<link rel="stylesheet" href="https://fonts.googleapis.com/css2?family=Kaushan+Script&family=Oleo+Script:wght@700&family=Passion+One:wght@700&family=Teko:wght@500&family=Yanone+Kaffeesatz:wght@400&display=swap">
<style>
  :root {
    --bg: #8f8f8f;
    --orange: #f08a1c;
    --orange-deep: #c9680f;
    --orange-soft: #f6a447;
    --gold: #ffc02a;
    --black: #141210;
    --green: #1d6b3a;
    --green-dark: #0f5230;
    --cream: #fbf4e6;
  }
  * { margin: 0; padding: 0; box-sizing: border-box; }
  html, body { width: 1200px; height: 1200px; overflow: hidden; background: var(--bg); }

  .pouch {
    position: absolute; left: 220px; top: 40px;
    width: 760px; height: 1120px;
    border-radius: 70px 70px 30px 30px;
    overflow: hidden;
    background: linear-gradient(180deg, var(--orange) 0%, var(--orange) 48%, var(--orange-deep) 62%, #3a2513 82%, var(--black) 100%);
  }

  .leaf-decor {
    position: absolute;
    background: radial-gradient(ellipse at center, rgba(120,70,20,0.45), rgba(120,70,20,0) 70%);
  }
  .leaf-decor--top { left: -40px; top: 0; width: 520px; height: 240px; }
  .leaf-decor--side { left: -60px; top: 540px; width: 420px; height: 360px; }

  .tagline-label {
    position: absolute; left: 160px; top: 95px; width: 460px; height: 78px;
    background: linear-gradient(180deg, #fff4e2, #f3c98f);
    border: 3px solid var(--black); border-radius: 8px;
    display: flex; align-items: center; justify-content: center;
    font-family: 'Kaushan Script', cursive; font-size: 36px; color: var(--black);
  }

  .stripe { position: absolute; left: 0; width: 100%; }
  .stripe--green-top { top: 238px; height: 10px; background: var(--green); }
  .stripe--orange-top { top: 248px; height: 8px; background: var(--orange); }
  .stripe--orange-bottom { top: 540px; height: 10px; background: var(--orange); }
  .stripe--green-bottom { top: 550px; height: 10px; background: var(--green); }

  .title-band {
    position: absolute; left: 0; top: 256px; width: 100%; height: 284px;
    background: linear-gradient(180deg, #201c18, var(--black));
    text-align: center;
  }
  .title-band__kicker {
    margin-top: 44px;
    font-family: 'Passion One', sans-serif; font-size: 68px; letter-spacing: 2px;
    color: var(--cream); line-height: 1;
  }
  .title-band__name {
    font-family: 'Oleo Script', cursive; font-size: 104px; line-height: 1.05;
    color: var(--cream); text-shadow: 5px 4px 0 var(--orange);
  }
  .title-band__benefits {
    margin-top: 10px;
    font-family: 'Teko', sans-serif; font-size: 40px; letter-spacing: 1px;
    color: var(--cream); display: flex; justify-content: center; align-items: center; gap: 12px;
  }
  .title-band__dot { width: 22px; height: 22px; border-radius: 50%; background: var(--orange-soft); }

  .brand {
    position: absolute; left: 140px; top: 600px;
    display: flex; align-items: center; gap: 12px;
  }
  .brand__circle { width: 34px; height: 34px; border-radius: 50%; background: var(--cream); }
  .brand__name {
    font-family: 'Teko', sans-serif; font-size: 40px; color: var(--cream); line-height: 1;
  }

  .map-australia {
    position: absolute; left: 440px; top: 660px; width: 280px; height: 250px;
    border-radius: 46% 40% 48% 42%;
    background: linear-gradient(160deg, var(--green) 0%, var(--green-dark) 100%);
  }

  .seed-window {
    position: absolute; left: 280px; top: 730px; width: 300px; height: 270px;
  }

  .features {
    position: absolute; left: 50px; top: 720px; width: 230px; list-style: none;
    font-family: 'Teko', sans-serif; font-size: 32px; color: var(--orange-soft);
  }
  .features li { border-bottom: 2px solid var(--orange-deep); line-height: 1.12; padding-top: 2px; }

  .origin {
    position: absolute; right: 30px; top: 870px; width: 220px; text-align: right;
    font-family: 'Yanone Kaffeesatz', sans-serif; color: var(--orange-soft); line-height: 1.1;
  }
  .origin__marker { width: 2px; height: 50px; background: var(--orange-soft); margin: 0 30px 8px auto; }
  .origin__label { font-size: 28px; font-style: italic; }
  .origin__weight { font-size: 42px; color: var(--gold); }
</style>
</head>
<body>
  <main class="pouch">
    <div class="leaf-decor leaf-decor--top" role="img" aria-label="Faint hemp leaf decoration"></div>
    <div class="tagline-label">Nature’s Perfect Super Food</div>

    <div class="stripe stripe--green-top"></div>
    <div class="stripe stripe--orange-top"></div>

    <section class="title-band">
      <p class="title-band__kicker">KERNEL OF</p>
      <h1 class="title-band__name">Field Seeds</h1>
      <p class="title-band__benefits">
        <span>TASTE GREAT</span><span class="title-band__dot"></span>
        <span>EASY TO USE</span><span class="title-band__dot"></span>
        <span>GOOD FOR YOU</span>
      </p>
    </section>

    <div class="stripe stripe--orange-bottom"></div>
    <div class="stripe stripe--green-bottom"></div>

    <div class="leaf-decor leaf-decor--side" role="img" aria-label="Faint hemp leaf decoration"></div>

    <div class="brand">
      <span class="brand__circle"></span>
      <span class="brand__name">Verdant Grain Collective</span>
    </div>

    <div class="map-australia" role="img" aria-label="Green map of Australia with Tasmania marked"></div>

    <svg class="seed-window" viewBox="0 0 300 270" role="img" aria-label="Photo of hulled hemp seeds in a heart-shaped window">
      <defs>
        <radialGradient id="seed-fill" cx="50%" cy="45%" r="60%">
          <stop offset="0%" stop-color="#e4dfc8"/>
          <stop offset="70%" stop-color="#b7b088"/>
          <stop offset="100%" stop-color="#7f7a4c"/>
        </radialGradient>
      </defs>
      <path d="M150 262 C60 190 6 140 6 78 C6 34 40 6 80 6 C114 6 138 26 150 52 C162 26 186 6 220 6 C260 6 294 34 294 78 C294 140 240 190 150 262 Z"
            fill="url(#seed-fill)" stroke="var(--green)" stroke-width="8"/>
    </svg>

    <ul class="features">
      <li>VEGAN</li>
      <li>PALEO</li>
      <li>RAW</li>
      <li>SUSTAINABLE</li>
      <li>HIGH IN PROTEIN</li>
      <li>HIGH IN OMEGA 3 + 6 EFA</li>
      <li>ANTI ALLERGENIC</li>
    </ul>

    <div class="origin">
      <div class="origin__marker"></div>
      <p class="origin__label">Premium Tasmanian Seed</p>
      <p class="origin__weight">500g</p>
    </div>
  </main>
</body>
</html>
```